Tilda Tinkerwire, An IT Company Has New Logo, Need Fresh Business Cards

IT company is called Tilda Tinkerwire and is displayed nicely with the new logo from here on pitchloft. Would like a fresh business card look that encompasses the idea that we want clients to Cherish Every Gadget. I love the use of circuitry with hearts as endpoints and x's and o's. It needs to have room for my certification logos of which there are 4 and a BRJ Alumni log. I am attaching my current card to illustrate how it has always captured attention, but that was in the early stages of business when I was doing more residential work. I am focused on businesses now, so a level of professionalism is necessary. I would also like the card to lend itself well to additional stationary, email signature, ticketing template for my workboard, etc. For the time being, I need the card for an upcoming conference so that work will come later. Color scheme should be that of the new logo. Thank you and I look forward to the designs.

Target Market(s)

Businesses looking for IT services.

Industry/Entity Type

Information Technology

Contact Information for Business Card

See above

Requirements
Must have
• New logo colors and a warm feel. Possibly a tad feminine as I am female, but appealing to males.
Nice to have
• I would like techy, but no too much so. I like friendly and connecting feels. People LOVED my old card and called me because it gave them a warm feeling.

```html
<!DOCTYPE html>
<html lang="en">
<head>
<meta charset="utf-8">
<title>Tilda Tinkerwire — Business Card</title>
<link href="https://fonts.googleapis.com/css2?family=Montserrat:wght@400;500&family=Quicksand:wght@400;500&display=swap" rel="stylesheet">
<style>
  :root {
    --backdrop: #222324;
    --card: #ffffff;
    --blue-deep: #0aa3e6;
    --blue-soft: #86cdea;
    --pink: #eea6cb;
    --green: #b8d66a;
    --ink: #2b2b2b;
  }
  * { margin: 0; padding: 0; box-sizing: border-box; }
  html, body { width: 1200px; height: 837px; overflow: hidden; background: var(--backdrop); }
  .canvas { position: relative; width: 1200px; height: 837px; }
  .card {
    position: absolute; left: 120px; top: 145px; width: 960px; height: 548px;
    background: var(--card); border-radius: 26px; overflow: hidden;
  }
  .band-deep { position: absolute; left: 0; top: 0; bottom: 0; width: 38px; background: var(--blue-deep); }
  .band-soft { position: absolute; left: 38px; top: 0; bottom: 0; width: 104px; background: var(--blue-soft); }
  .edge-pink { position: absolute; right: 0; top: 0; bottom: 0; width: 14px; background: var(--pink); }
  .brand {
    position: absolute; left: 470px; top: 120px;
    display: flex; align-items: center; gap: 16px; white-space: nowrap;
  }
  .brand-dot { width: 22px; height: 22px; border-radius: 50%; background: var(--blue-soft); }
  .brand-name {
    font-family: "Quicksand", sans-serif; font-weight: 500; font-size: 40px; color: var(--blue-soft);
  }
  .tagline {
    position: absolute; left: 360px; top: 205px; white-space: nowrap;
    font-family: "Quicksand", sans-serif; font-weight: 400; font-size: 22px;
    letter-spacing: 8px; color: var(--pink); text-transform: uppercase;
  }
  .contacts { position: absolute; left: 200px; top: 300px; list-style: none; }
  .contact { display: flex; align-items: center; gap: 22px; height: 62px; white-space: nowrap; }
  .contact-icon {
    width: 44px; height: 44px; border-radius: 50%; background: var(--blue-deep);
    display: flex; align-items: center; justify-content: center; flex: none;
  }
  .contact-text { font-family: "Montserrat", sans-serif; font-size: 22px; color: var(--ink); }
  .circuit-art {
    position: absolute; right: 14px; bottom: 0; width: 330px; height: 190px;
    background: linear-gradient(120deg, rgba(238,166,203,.18), rgba(134,205,234,.2) 50%, rgba(184,214,106,.18));
  }
</style>
</head>
<body>
<div class="canvas">
  <section class="card">
    <div class="band-deep"></div>
    <div class="band-soft"></div>
    <div class="edge-pink"></div>

    <div class="brand">
      <span class="brand-dot"></span>
      <span class="brand-name">Tilda Tinkerwire</span>
    </div>

    <p class="tagline">×○ Cherish Every Gadget ○×</p>

    <ul class="contacts">
      <li class="contact">
        <span class="contact-icon">
          <svg width="22" height="22" viewBox="0 0 24 24"><path d="M6.6 10.8a15 15 0 0 0 6.6 6.6l2.2-2.2a1 1 0 0 1 1-.25 11.4 11.4 0 0 0 3.6.57 1 1 0 0 1 1 1V20a1 1 0 0 1-1 1A17 17 0 0 1 3 4a1 1 0 0 1 1-1h3.5a1 1 0 0 1 1 1c0 1.25.2 2.45.57 3.57a1 1 0 0 1-.25 1z" fill="#fff"/></svg>
        </span>
        <span class="contact-text">+407 555 0148</span>
      </li>
      <li class="contact">
        <span class="contact-icon">
          <svg width="22" height="22" viewBox="0 0 24 24"><rect x="3" y="6" width="18" height="12" rx="1.5" fill="#fff"/><path d="M3.5 6.5 12 13l8.5-6.5" fill="none" stroke="#0aa3e6" stroke-width="1.6"/></svg>
        </span>
        <span class="contact-text">hello@tilda-tinkerwire.com</span>
      </li>
      <li class="contact">
        <span class="contact-icon">
          <svg width="22" height="22" viewBox="0 0 24 24" fill="none" stroke="#fff" stroke-width="1.6"><circle cx="12" cy="12" r="9"/><ellipse cx="12" cy="12" rx="4" ry="9"/><path d="M3 12h18M4.5 7.5h15M4.5 16.5h15"/></svg>
        </span>
        <span class="contact-text">www.tilda-tinkerwire.com</span>
      </li>
    </ul>

    <div class="circuit-art" role="img" aria-label="Faint pastel circuit-trace decoration in pink, blue and green"></div>
  </section>
</div>
</body>
</html>
```